Protrait photographers business card

Need a new catchy, chic business card to promote my new portrait photograghy business. Love taking the natural, location portraits of families, children, teens. It should look classy, but also warm & friendly. I want it to show that Famliy, friends, couples & childten are what I love photographing, so if it can have that sort of feel to it & also looking energetic.

Target Market(s)

Families, couples, babies, people on holidays wanting some locational professional photos

Industry/Entity Type

Portrait Photography

Contact Information for Business Card

Lumivale photography, By Tavi, Norah Balfrey,Ph: 0487356024, Kestrel cove, Qld

Font styles to use
Decorative
Script

Requirements
Must have
• Company name & photographers name
Nice to have
• a coloured card
Should not have
• not be on a white card

```html
<!DOCTYPE html>
<html lang="en">
<head>
<meta charset="utf-8">
<title>Lumivale Photography – Business Card</title>
<link rel="stylesheet" href="https://fonts.googleapis.com/css2?family=Bodoni+Moda:wght@500&family=Raleway:wght@300;400&display=swap">
<style>
  :root {
    --backdrop: #b3b4b4;
    --backdrop-light: #c4c5c5;
    --card-coral: #d3534a;
    --card-ink: #f6ece8;
    --card-line: rgba(246, 236, 232, 0.8);
  }
  * { margin: 0; padding: 0; box-sizing: border-box; }
  html, body {
    width: 1200px;
    height: 900px;
    overflow: hidden;
  }
  body {
    background: radial-gradient(ellipse at 50% 40%, var(--backdrop-light), var(--backdrop));
    display: flex;
    align-items: center;
    justify-content: center;
  }
  .business-card {
    position: relative;
    width: 900px;
    height: 514px;
    background: var(--card-coral);
    color: var(--card-ink);
    box-shadow: 0 18px 40px rgba(0, 0, 0, 0.18);
  }
  .card-lines {
    position: absolute;
    inset: 0;
    width: 100%;
    height: 100%;
  }
  .brand-name {
    position: absolute;
    left: 90px;
    top: 150px;
    width: 250px;
    font-family: "Raleway", sans-serif;
    font-weight: 300;
    font-size: 30px;
    line-height: 1.15;
    letter-spacing: 0.12em;
    text-transform: uppercase;
    text-align: center;
  }
  .brand-name .brand-sub {
    display: block;
    text-transform: none;
    letter-spacing: 0.06em;
    font-size: 30px;
  }
  .photographer-name {
    position: absolute;
    left: 380px;
    top: 195px;
    font-family: "Bodoni Moda", serif;
    font-weight: 500;
    font-size: 42px;
    letter-spacing: 0.01em;
  }
  .contact-details {
    position: absolute;
    left: 382px;
    top: 268px;
    font-family: "Raleway", sans-serif;
    font-weight: 300;
    font-size: 22px;
    line-height: 1.5;
    list-style: none;
  }
</style>
</head>
<body>
  <article class="business-card">
    <svg class="card-lines" viewBox="0 0 900 514" aria-hidden="true">
      <line x1="560" y1="190" x2="880" y2="170" stroke="var(--card-line)" stroke-width="1.2"/>
      <line x1="690" y1="200" x2="880" y2="188" stroke="var(--card-line)" stroke-width="1.2"/>
      <line x1="130" y1="360" x2="330" y2="340" stroke="var(--card-line)" stroke-width="1.2"/>
    </svg>

    <h1 class="brand-name">Lumivale <span class="brand-sub">photography</span></h1>

    <h2 class="photographer-name">Norah Balfrey</h2>

    <ul class="contact-details">
      <li class="contact-phone">Ph: 0487356024</li>
      <li class="contact-location">Kestrel cove, Qld</li>
    </ul>
  </article>
</body>
</html>
```